Young Up and Coming Contractor Needs a Super Cool Website

I need a progressive, creative, and edgy website for my construction company. I've been in business since 2014 in Madison Wisconsin. I do residential and commercial projects to include new construction, renovation, remodel of kitchen and baths, tile, drywall, and flooring. I want the website to represent what I do or the essence of my company. I need for you to give me a website that says I'm in the business of building, fixing, and remaking bricks and mortar. I would like to see designs that communicate quality craftsmanship from a talented young contractor. The company is The Marendale Company, Marendale.
Updates

Need extra days to review

Went on vacation/holiday

Target Market(s)

Residential and commercial clients in need of remodeling, renovation, and new construction.

Coding

Coded - Design and coding required

Number of Pages Required

4 page

Font styles to use
Sans Serif

Colors

Designer to choose colors to be used in the design.

Requirements
Must have
• I would like the website to have four pages to include Home, About, Projects, Contact. I want the design to reflect a younger more progressive vibe while still portraying a professional image. I'm looking for a clean modern design that appeals to both residential and commercial clientele.
Should not have
• Please don't make it boring.

```html
<!DOCTYPE html>
<html lang="en">
<head>
<meta charset="utf-8">
<title>Marendale Remodeling</title>
<link rel="stylesheet" href="https://fonts.googleapis.com/css2?family=Fira+Sans:wght@400;500;600;700&family=Lato:wght@400;700&display=swap">
<style>
:root{
  --green:#8cc63f;
  --green-dark:#76ad2c;
  --ink:#222222;
  --text:#444444;
  --muted:#666666;
  --light:#e8e8e8;
  --dark:#333333;
  --darker:#2a2a2a;
  --white:#ffffff;
}
*{margin:0;padding:0;box-sizing:border-box}
html,body{width:1200px;height:3482px;overflow:hidden}
body{font-family:"Lato",sans-serif;color:var(--text);background:var(--white);position:relative}
.abs{position:absolute}
h1,h2,h3,.brand{font-family:"Fira Sans",sans-serif}

/* top bar */
.topbar{top:0;left:0;width:1200px;height:42px;border-bottom:1px solid #e3e3e3;font-size:15px;color:var(--ink)}
.topbar .item{top:12px;display:flex;align-items:center;gap:10px;white-space:nowrap}
.topbar svg{width:16px;height:16px}
.socials{top:14px;left:1040px;display:flex;gap:12px}
.socials span{width:12px;height:12px;border-radius:50%;background:#555}

/* nav */
.nav{top:42px;left:0;width:1200px;height:113px}
.brand-mark{left:77px;display:flex;align-items:center;gap:12px}
.brand-mark .sq{width:40px;height:40px;background:var(--green)}
.brand-mark .brand{font-size:34px;font-weight:700;color:var(--green);line-height:1;letter-spacing:.5px}
.menu{right:77px;display:flex;gap:40px;font-size:16px;color:var(--ink);font-family:"Fira Sans",sans-serif}
.menu a{color:inherit;text-decoration:none;position:relative;white-space:nowrap}
.menu a.active{color:var(--green)}
.menu a.active::after{content:"";position:absolute;left:-6px;right:-6px;top:64px;height:3px;background:var(--green)}

/* hero */
.hero{top:155px;left:0;width:1200px;height:576px;background:linear-gradient(120deg,#6a6a55 0%,#4a4a3e 35%,#8a8160 60%,#3f463a 100%)}
.hero::after{content:"";position:absolute;inset:0;background:rgba(0,0,0,.35)}
.hero-copy{position:absolute;z-index:1;left:0;width:1200px;top:203px;text-align:center;color:var(--white)}
.hero-copy h1{font-size:46px;font-weight:600;letter-spacing:1px}
.hero-copy .rule{width:90px;height:3px;background:var(--white);margin:14px auto 18px}
.hero-copy p{font-size:19px;line-height:28px;width:560px;margin:0 auto}
.hero-btns{display:flex;justify-content:center;gap:12px;margin-top:32px}
.btn{height:46px;padding:0 26px;display:flex;align-items:center;justify-content:center;font-size:18px;font-family:"Fira Sans",sans-serif;color:var(--white);text-transform:uppercase;white-space:nowrap}
.btn-green{background:var(--green);min-width:178px}
.btn-ghost{border:2px solid var(--white);min-width:178px}

/* who we are */
.about-photo-back{top:792px;left:77px;width:313px;height:415px;background:linear-gradient(160deg,#c9a23a,#5a4a2a 60%,#2e2a24)}
.about-frame{top:800px;left:85px;width:297px;height:399px;border:2px solid rgba(255,255,255,.7)}
.about-photo-front{top:863px;left:239px;width:225px;height:316px;background:linear-gradient(150deg,#d9c9a8,#b78a4a 50%,#3b3127)}
.about-frame2{top:873px;left:249px;width:205px;height:296px;border:2px solid rgba(255,255,255,.75)}
.about-copy{top:866px;left:557px;width:560px}
.about-copy h2{font-size:38px;font-weight:600;color:var(--ink);letter-spacing:1px;margin-bottom:22px}
.about-copy p{font-size:15px;line-height:26px;color:var(--ink);margin-bottom:6px}
.about-copy .more{font-size:15px;color:var(--ink);text-decoration:underline;font-weight:700;display:inline-block;margin-top:12px}

/* offer */
.offer{top:1281px;left:0;width:1200px;height:448px;background:var(--light)}
.section-title{left:0;width:1200px;text-align:center;font-size:38px;font-weight:600;color:var(--ink);letter-spacing:1px}
.service{width:300px;text-align:center;top:139px}
.service .icon{width:104px;height:104px;background:var(--green);margin:0 auto 20px;display:flex;align-items:center;justify-content:center}
.service h3{font-size:24px;font-weight:400;color:var(--ink);margin-bottom:8px}
.service p{font-size:15px;line-height:25px;color:var(--ink)}

/* projects */
.projects{top:1729px;left:0;width:1200px;height:585px;background:linear-gradient(120deg,#2b2a26,#3d3a33 50%,#23221f)}
.projects .section-title{color:var(--white);top:52px}
.filters{top:146px;left:0;width:1200px;display:flex;justify-content:center;align-items:center;gap:32px;font-size:15px;color:#bdbdbd;letter-spacing:1px}
.filters .dash{width:36px;height:2px;background:var(--green)}
.filters .on{color:var(--white)}
.tile{top:200px;width:262px;height:248px}
.tile-hl{border:6px solid var(--green);background:#3a3a3a;display:flex;flex-direction:column;align-items:center;justify-content:center;gap:16px;color:var(--white);font-size:26px;font-family:"Fira Sans",sans-serif}
.arrow{top:486px;width:26px;height:28px;background:rgba(255,255,255,.15);display:flex;align-items:center;justify-content:center}

/* blog */
.blog-title{top:2358px}
.ghost-word{font-family:"Fira Sans",sans-serif;font-size:40px;color:#ececec;font-weight:500}
.testimonial{top:2495px;left:77px;width:480px;height:522px;border:1px solid #d6d6d6;text-align:center;padding:0 50px}
.testimonial h3{font-size:20px;font-weight:500;color:var(--ink);margin-top:82px;margin-bottom:18px}
.testimonial p{font-size:14px;line-height:25px;color:var(--muted)}
.avatar{width:104px;height:104px;border-radius:50%;background:linear-gradient(160deg,#c9d6e0,#5d87a8);margin:38px auto 14px}
.client{color:var(--green);font-size:15px;font-weight:700}
.dots{display:flex;justify-content:center;gap:5px;margin-top:16px}
.dots span{width:15px;height:15px;border-radius:50%;border:2px solid var(--green)}
.dots span.on{background:var(--green)}
.post-img{left:768px;width:355px;height:272px}
.post-card{left:599px;width:306px;height:214px;background:var(--white);border:1px solid #e1e1e1;box-shadow:0 2px 10px rgba(0,0,0,.12);padding:34px 34px 0}
.post-card .meta{font-size:15px;color:var(--ink);padding-bottom:12px;border-bottom:1px solid #ddd;margin-bottom:14px}
.post-card p{font-size:14px;line-height:23px;color:var(--muted)}
.post-card .read{display:block;text-align:right;color:var(--green-dark);font-size:14px;margin-top:14px}

/* footer */
.footer{top:3122px;left:0;width:1200px;height:294px;background:var(--dark)}
.foot-logo{top:-16px;left:77px;width:322px;height:144px;background:#3f3f3f;display:flex;align-items:center;justify-content:center;gap:14px}
.foot-logo .sq{width:36px;height:36px;background:var(--green)}
.foot-logo .brand{font-size:34px;font-weight:700;color:var(--white);letter-spacing:.5px}
.foot-h{font-family:"Fira Sans",sans-serif;font-size:20px;font-weight:600;color:var(--green);letter-spacing:.5px}
.newsletter-h{color:var(--white);font-size:17px;top:160px;left:77px}
.email{top:197px;left:77px;width:322px;height:47px;border:1px solid #666;display:flex;align-items:center;justify-content:space-between;padding:0 14px;color:#999;font-size:14px}
.list{list-style:none;font-size:15px;color:var(--white)}
.list li{display:flex;align-items:center;gap:14px;height:36px;white-space:nowrap}
.list svg{flex:none}
.contact li{align-items:flex-start;height:auto;margin-bottom:24px;line-height:23px}
.bottombar{top:3416px;left:0;width:1200px;height:66px;background:var(--darker);color:var(--white);font-size:14px}
.bottombar p{position:absolute;left:77px;top:24px}
.to-top{position:absolute;left:1074px;top:9px;width:48px;height:48px;border-radius:50%;border:2px solid var(--green);display:flex;align-items:center;justify-content:center}
</style>
</head>
<body>

<header class="topbar abs">
  <div class="item abs" style="left:77px">
    <svg viewBox="0 0 16 16"><path d="M3 1l3 3-2 2a9 9 0 006 6l2-2 3 3-2 2C6 15 1 10 1 3z" fill="#8cc63f"/></svg>
    Call Us Now 123 456 7890
  </div>
  <div class="item abs" style="left:346px">
    <svg viewBox="0 0 16 16"><rect x="1" y="3" width="14" height="10" fill="#8cc63f"/><path d="M1 3l7 6 7-6" stroke="#fff" stroke-width="1.4" fill="none"/></svg>
    hello@marendalebuilds.com
  </div>
  <div class="socials abs"><span></span><span></span><span></span><span></span></div>
</header>

<nav class="nav abs">
  <div class="brand-mark abs" style="top:20px"><span class="sq"></span><span class="brand">MARENDALE</span></div>
  <div class="menu abs" style="top:44px">
    <a class="active" href="#">HOME</a><a href="#">ABOUT</a><a href="#">PROJECTS</a><a href="#">CONTACT</a>
  </div>
</nav>

<section class="hero abs" role="img" aria-label="Construction workers in hard hats reviewing building plans">
  <div class="hero-copy">
    <h1>DESIGN YOUR DREAMS WITH US</h1>
    <div class="rule"></div>
    <p>Creating a sustainable future through building preservation green architecture, and smart design</p>
    <div class="hero-btns"><span class="btn btn-green">Contact Us</span><span class="btn btn-ghost">View Projects</span></div>
  </div>
</section>

<section class="about">
  <div class="about-photo-back abs" role="img" aria-label="Worker operating drilling machinery"></div>
  <div class="about-frame abs"></div>
  <div class="about-photo-front abs" role="img" aria-label="Contractor showing plans to a client"></div>
  <div class="about-frame2 abs"></div>
  <div class="about-copy abs">
    <h2>WHO WE ARE</h2>
    <p>Lorem Ipsum is simply dummy text of the printing and typesetting industry. Lorem Ipsum has been the industry's standard dummy text ever since the 1500s, when an unknown printer took a galley of type and scrambled it to make a type specimen book. It has survived not only five centuries.</p>
    <p>Lorem Ipsum is simply dummy text of the printing and typesetting industry. Lorem Ipsum has been the industry's standard dummy text ever since.</p>
    <span class="more">READ MORE</span>
  </div>
</section>

<section class="offer abs">
  <h2 class="section-title abs" style="top:50px">WHAT WE OFFER</h2>
  <div class="service abs" style="left:87px">
    <div class="icon"><svg width="56" height="56" viewBox="0 0 56 56" fill="#fff"><circle cx="28" cy="16" r="8"/><path d="M12 46c0-10 7-16 16-16s16 6 16 16z"/><rect x="16" y="9" width="24" height="4"/></svg></div>
    <h3>Residential</h3>
    <p>Lorem Ipsum is simply dummy text of the printing and typesetting industry. Lorem Ipsum has been the industry</p>
  </div>
  <div class="service abs" style="left:449px">
    <div class="icon"><svg width="56" height="56" viewBox="0 0 56 56" fill="none" stroke="#fff" stroke-width="4"><path d="M8 28L28 10l20 18"/><path d="M14 24v22h28V24"/><path d="M22 46V34h12v12"/></svg></div>
    <h3>Commercial</h3>
    <p>Lorem Ipsum is simply dummy text of the printing and typesetting industry. Lorem Ipsum has been the industry</p>
  </div>
  <div class="service abs" style="left:811px">
    <div class="icon"><svg width="56" height="56" viewBox="0 0 56 56" fill="#fff"><path d="M6 28L28 8l22 20h-6v20H12V28z"/><rect x="23" y="32" width="10" height="16" fill="#8cc63f"/></svg></div>
    <h3>Interior design</h3>
    <p>Lorem Ipsum is simply dummy text of the printing and typesetting industry. Lorem Ipsum has been the industry</p>
  </div>
</section>

<section class="projects abs" role="img" aria-label="Dark photo of a construction crew behind the project gallery">
  <h2 class="section-title abs">LASTEST PROJECTS</h2>
  <div class="filters abs"><span class="dash"></span><span class="on">ALL</span><span>RESIDENTIAL</span><span>COMMERCIAL</span><span class="dash"></span></div>
  <div class="tile abs" style="left:77px;background:linear-gradient(180deg,#c9d6e2,#2b2b2b 55%,#6b7a5a)" role="img" aria-label="Modern black curved office building"></div>
  <div class="tile abs" style="left:339px;background:linear-gradient(135deg,#e8eef3,#8fa8bd 50%,#3f5a74)" role="img" aria-label="Glass skyscraper facade"></div>
  <div class="tile tile-hl abs" style="left:601px">
    <svg width="40" height="24" viewBox="0 0 40 24"><path d="M2 12C8 3 32 3 38 12 32 21 8 21 2 12z" fill="none" stroke="#fff" stroke-width="2.5"/><circle cx="20" cy="12" r="5" fill="#fff"/></svg>
    <span>Residential</span>
    <svg width="30" height="30" viewBox="0 0 30 30" fill="none" stroke="#fff" stroke-width="3"><path d="M13 17l-5 5a3.5 3.5 0 01-5-5l5-5"/><path d="M17 13l5-5a3.5 3.5 0 00-5-5l-5 5"/><path d="M11 19l8-8"/></svg>
  </div>
  <div class="tile abs" style="left:863px;width:260px;background:linear-gradient(180deg,#8fc0e8,#b9a98c 50%,#5c7a3f)" role="img" aria-label="Large suburban family house"></div>
  <div class="arrow abs" style="left:80px"><svg width="10" height="14" viewBox="0 0 10 14"><path d="M8 1L2 7l6 6" stroke="#fff" stroke-width="2" fill="none"/></svg></div>
  <div class="arrow abs" style="left:1094px"><svg width="10" height="14" viewBox="0 0 10 14"><path d="M2 1l6 6-6 6" stroke="#fff" stroke-width="2" fill="none"/></svg></div>
</section>

<section class="blog">
  <h2 class="section-title blog-title abs">BLOG &amp; TESTIMONIALS</h2>
  <span class="ghost-word abs" style="left:77px;top:2434px">Testimonials</span>
  <div class="testimonial abs">
    <h3>Lorem Ipsum is simply dummy!</h3>
    <p>Lorem Ipsum is simply dummy text of the printing and typesetting industry. Lorem Ipsum has been the industry's standard dummy text ever since the 1500s, when an unknown printer took a galley.</p>
    <div class="avatar" role="img" aria-label="Client portrait"></div>
    <div class="client">- Client Name</div>
    <div class="dots"><span class="on"></span><span></span><span></span></div>
  </div>
  <div class="post-img abs" style="top:2444px;background:linear-gradient(160deg,#9fc6e6,#d8c9a0 50%,#c6b04a)" role="img" aria-label="Engineers in hard hats reviewing plans on site"></div>
  <div class="post-card abs" style="top:2490px">
    <div class="meta">posted by admin, 20/12/17</div>
    <p>Lorem Ipsum is simply dummy text of the printing.</p>
    <span class="read">Read More</span>
  </div>
  <div class="post-img abs" style="top:2746px;background:linear-gradient(160deg,#5a7aa8,#b58a5a 55%,#d07a2a)" role="img" aria-label="Construction workers in safety vests studying drawings"></div>
  <div class="post-card abs" style="top:2792px">
    <div class="meta">posted by admin, 20/12/17</div>
    <p>Lorem Ipsum is simply dummy text of the printing.</p>
    <span class="read">Read More</span>
  </div>
  <span class="ghost-word abs" style="left:1021px;top:3030px">Blog</span>
</section>

<footer class="footer abs">
  <div class="foot-logo abs"><span class="sq"></span><span class="brand">MARENDALE</span></div>
  <h3 class="foot-h newsletter-h abs">NEWSLETTER SIGNUP</h3>
  <div class="email abs">Email Address
    <svg width="28" height="22" viewBox="0 0 28 22"><path d="M1 10L27 1 20 21 14 13z" fill="#8cc63f"/></svg>
  </div>
  <h3 class="foot-h abs" style="left:453px;top:62px">OUR SERVICES</h3>
  <ul class="list abs" style="left:453px;top:102px">
    <li><svg width="14" height="14" viewBox="0 0 14 14"><circle cx="7" cy="7" r="6" stroke="#8cc63f" fill="none" stroke-width="1.5"/><path d="M6 4l3 3-3 3" stroke="#8cc63f" fill="none" stroke-width="1.5"/></svg>Construction</li>
    <li><svg width="14" height="14" viewBox="0 0 14 14"><circle cx="7" cy="7" r="6" stroke="#8cc63f" fill="none" stroke-width="1.5"/><path d="M6 4l3 3-3 3" stroke="#8cc63f" fill="none" stroke-width="1.5"/></svg>Remodel</li>
    <li><svg width="14" height="14" viewBox="0 0 14 14"><circle cx="7" cy="7" r="6" stroke="#8cc63f" fill="none" stroke-width="1.5"/><path d="M6 4l3 3-3 3" stroke="#8cc63f" fill="none" stroke-width="1.5"/></svg>Renovation</li>
    <li><svg width="14" height="14" viewBox="0 0 14 14"><circle cx="7" cy="7" r="6" stroke="#8cc63f" fill="none" stroke-width="1.5"/><path d="M6 4l3 3-3 3" stroke="#8cc63f" fill="none" stroke-width="1.5"/></svg>Flooring</li>
  </ul>
  <h3 class="foot-h abs" style="left:801px;top:62px">CONTACT INFO</h3>
  <ul class="list contact abs" style="left:801px;top:108px">
    <li><svg width="16" height="20" viewBox="0 0 16 20"><path d="M8 1a7 7 0 00-7 7c0 5 7 11 7 11s7-6 7-11a7 7 0 00-7-7z" fill="#8cc63f"/><circle cx="8" cy="8" r="2.5" fill="#333"/></svg><span>Lorem ipsum dolor sit amet,<br>consectetur adipiscing elit.</span></li>
    <li><svg width="16" height="16" viewBox="0 0 16 16"><path d="M3 1l3 3-2 2a9 9 0 006 6l2-2 3 3-2 2C6 15 1 10 1 3z" fill="#8cc63f"/></svg>123 456 7890</li>
    <li><svg width="16" height="14" viewBox="0 0 16 14"><rect x="1" y="2" width="14" height="10" fill="none" stroke="#8cc63f" stroke-width="1.5"/><path d="M1 2l7 6 7-6" stroke="#8cc63f" stroke-width="1.5" fill="none"/></svg>hello@marendalebuilds.com</li>
  </ul>
</footer>

<div class="bottombar abs">
  <p>2018 ©MARENDALE REMODELING- All Rights Reserved.</p>
  <div class="to-top"><svg width="16" height="10" viewBox="0 0 16 10"><path d="M1 9l7-7 7 7" stroke="#fff" stroke-width="2" fill="none"/></svg></div>
</div>

</body>
</html>
```